Tech business card design

We need an amazing business card design for our new business 'Brakka' a marketing tech startup based in Sydney, Australia. We provide an online marketplace for businesses to search and buy advertising media, connect with service providers and learn more about marketing. We wish to communicate 'cool tech', reliability and professionalism and design based around our logo.

Target Market(s)

Business Owners

Contact Information for Business Card

Name
Position
Email Address
Website
Phone Number

Font styles to use
Other font styles liked:
• Avenir & Avenir Next

Colors

Designer to choose colors to be used in the design.

```html
<!DOCTYPE html>
<html lang="en">
<head>
<meta charset="utf-8">
<title>Brakka business card</title>
<link rel="stylesheet" href="https://fonts.googleapis.com/css2?family=Nunito+Sans:wght@400;600;800&display=swap">
<style>
  :root {
    --navy: #15153f;
    --navy-deep: #0f0f33;
    --paper: #e6e6e6;
    --card-white: #ffffff;
    --ink-grey: #5b5b66;
    --rule-grey: #c9c9cf;
  }
  * { margin: 0; padding: 0; box-sizing: border-box; }
  html, body {
    width: 1125px;
    height: 1200px;
    overflow: hidden;
  }
  body {
    background: var(--paper);
    font-family: "Nunito Sans", "Avenir Next", Avenir, sans-serif;
    position: relative;
  }
  .card {
    position: absolute;
    left: 171px;
    width: 826px;
  }
  /* Front */
  .card-front {
    top: 106px;
    height: 472px;
    background: var(--card-white);
  }
  .card-front .base-line {
    position: absolute;
    left: 0; right: 0;
    top: 448px;
    height: 3px;
    background: var(--rule-grey);
  }
  .card-front .base-band {
    position: absolute;
    left: 0; right: 0;
    bottom: 0;
    height: 19px;
    background: var(--navy);
  }
  .wordmark {
    position: absolute;
    font-weight: 800;
    letter-spacing: -0.01em;
    line-height: 1;
  }
  .card-front .wordmark {
    left: 96px;
    top: 178px;
    font-size: 96px;
    color: var(--navy);
  }
  .divider {
    position: absolute;
    left: 420px;
    top: 157px;
    width: 2px;
    height: 160px;
    background: linear-gradient(to bottom, rgba(150,150,160,0), #9a9aa4 40%, #9a9aa4 60%, rgba(150,150,160,0));
  }
  .identity {
    position: absolute;
    left: 459px;
    top: 158px;
  }
  .identity .person-name {
    font-size: 29px;
    font-weight: 600;
    color: var(--navy);
    line-height: 1.1;
  }
  .identity .person-role {
    font-size: 20px;
    color: var(--ink-grey);
    letter-spacing: 0.02em;
    line-height: 1.2;
  }
  .contact-list {
    list-style: none;
    margin-top: 22px;
  }
  .contact-list li {
    display: flex;
    align-items: center;
    gap: 12px;
    font-size: 19px;
    color: var(--ink-grey);
    height: 26px;
  }
  .contact-list svg {
    width: 18px;
    height: 18px;
    flex: none;
  }
  /* Back */
  .card-back {
    top: 639px;
    height: 471px;
    background: radial-gradient(ellipse at center, #1d1d4f 0%, var(--navy) 55%, var(--navy-deep) 100%);
  }
  .card-back .wordmark {
    left: 0; right: 0;
    top: 162px;
    text-align: center;
    font-size: 150px;
    color: #ffffff;
  }
  .card-back .web-address {
    position: absolute;
    left: 0; right: 0;
    top: 384px;
    text-align: center;
    font-size: 19px;
    letter-spacing: 0.5em;
    color: #ffffff;
  }
</style>
</head>
<body>
  <section class="card card-front">
    <div class="wordmark">brakka</div>
    <div class="divider"></div>
    <div class="identity">
      <p class="person-name">DANIEL REEVE</p>
      <p class="person-role">FOUNDER, DIRECTOR</p>
      <ul class="contact-list">
        <li>
          <svg viewBox="0 0 18 18" aria-hidden="true"><rect x="4.5" y="1" width="9" height="16" rx="1.5" fill="none" stroke="#3b3b48" stroke-width="1.6"/><line x1="7.5" y1="14.5" x2="10.5" y2="14.5" stroke="#3b3b48" stroke-width="1.4"/></svg>
          +61 (0)412 555 208
        </li>
        <li>
          <svg viewBox="0 0 18 18" aria-hidden="true"><rect x="2" y="5" width="14" height="9" fill="#3b3b48"/><polyline points="2,5 9,10.5 16,5" fill="none" stroke="#ffffff" stroke-width="1.2"/></svg>
          daniel@brakkamedia.com.au
        </li>
        <li>
          <svg viewBox="0 0 18 18" aria-hidden="true"><circle cx="9" cy="9" r="7.5" fill="#3b3b48"/><path d="M5 6.5 Q8 5 9 8 Q7 10 9 12 L8 15 M11 4 Q13 7 12.5 9 Q14 11 13.5 13" fill="none" stroke="#ffffff" stroke-width="1.2"/></svg>
          www.brakkamedia.com.au
        </li>
      </ul>
    </div>
    <div class="base-line"></div>
    <div class="base-band"></div>
  </section>

  <section class="card card-back">
    <div class="wordmark">brakka</div>
    <p class="web-address">www.brakkamedia.com.au</p>
  </section>
</body>
</html>
```